Infographic Table of AI Pricing Options for LinkedIn post

Turn this table (in the powerpoint slide attached) into an attractively formatted infographic table for Strelquin (www.strelquin.com).
This will be an infographic displayed on a linkedin post from a consultant from Strelquin.
Try to keep it on brand with Strelquin look and feel.

Target Market(s)

Tech and SaaS CEOs and Founders; Private Equity and Venture Capital employees

Industry/Entity Type

Management Consulting

Colors
0054AA
0677BA
7BADD7
CADEEF
E8F1F8

```html
<!DOCTYPE html>
<html lang="en">
<head>
<meta charset="utf-8">
<title>Strelquin – Challenges of GenAI Monetization</title>
<link href="https://fonts.googleapis.com/css2?family=Manrope:wght@400;500;600;700;800&display=swap" rel="stylesheet">
<style>
:root{
  --bg:#101b25;
  --panel:#15232f;
  --label-band:#0f1921;
  --divider:#0f1a23;
  --white:#ffffff;
  --muted:#e3ebf1;
  --blue-sub:#4aa3c8;
  --teal-sub:#7fc9b0;
  --c1-head:#4ea8d9;--c1-body:#1d3a52;
  --c2-head:#2a82b9;--c2-body:#173e5b;
  --c3-head:#38aaa5;--c3-body:#1f4852;
  --c4-head:#2e5e7e;--c4-body:#253441;
  --tick:#4cc46b;
  --cross:#3d90d6;
}
*{margin:0;padding:0;box-sizing:border-box}
html,body{width:1200px;height:927px;overflow:hidden;background:var(--bg)}
body{font-family:"Manrope",sans-serif;color:var(--white);position:relative}
.headline{position:absolute;left:68px;top:58px;font-weight:400;font-size:38px;line-height:43px;letter-spacing:-0.9px}
.headline b{font-weight:800}
.brand{position:absolute;left:884px;top:60px;display:flex;align-items:center;gap:12px;font-weight:500;font-size:37px;letter-spacing:-0.3px}
.brand-mark{width:48px;height:48px;background:var(--c1-head);border-radius:6px}
.panel{position:absolute;left:68px;top:228px;width:1066px;height:640px;background:var(--panel);border-radius:26px}
.tag-shadow{position:absolute;left:126px;top:232px;width:481px;height:46px;background:#0b141b;border-radius:8px}
.tag{position:absolute;left:136px;top:226px;width:470px;height:46px;border-radius:8px;background:linear-gradient(90deg,#4aa3d8,#63c7bb);font-weight:700;font-size:26.5px;letter-spacing:-0.2px;display:flex;align-items:center;justify-content:center}
.group-label{position:absolute;top:296px;font-size:15.5px;font-weight:500}
.group-label.now{left:266px;color:var(--blue-sub)}
.group-label.future{right:90px;color:var(--teal-sub)}
.row-band{position:absolute;left:68px;width:194px;background:var(--label-band)}
.row-label{position:absolute;left:70px;font-weight:700;font-size:21px;letter-spacing:0.2px}
.col{position:absolute;top:334px;width:206px;height:518px;border-radius:12px;overflow:hidden}
.col-head{height:64px;padding-top:4px;display:flex;align-items:center;justify-content:center;text-align:center;font-weight:700;font-size:20px;line-height:23px}
.col .cell{position:absolute;left:0;right:0;padding:0 30px 0 19px;font-size:12px;line-height:17px;font-weight:500;color:var(--muted)}
.cell.desc{top:80px}
.cell.ex{top:151px;height:88px;border-top:2px solid var(--divider);display:flex;flex-direction:column;align-items:center;justify-content:center;gap:16px;padding:0 8px}
.cell.pros{top:239px;height:120px;border-top:2px solid var(--divider);padding-top:13px;padding-left:22px}
.cell.cons{top:359px;border-top:2px solid var(--divider);padding-top:13px;padding-left:22px}
.ex-name{display:flex;align-items:center;gap:6px;font-weight:700;font-size:14px;color:var(--white);white-space:nowrap}
.ex-name.lg{font-size:19px}
.ex-name i{width:22px;height:22px;background:#5e8da8;border-radius:4px;display:inline-block}
ul{list-style:none}
li{display:flex;gap:10px;margin-bottom:11px;line-height:15px}
li svg{flex:none;width:14px;height:14px;margin-top:0}
.c1{left:265px;background:var(--c1-body)}.c1 .col-head{background:var(--c1-head)}
.c2{left:480px;background:var(--c2-body)}.c2 .col-head{background:var(--c2-head)}
.c3{left:695px;background:var(--c3-body)}.c3 .col-head{background:var(--c3-head)}
.c4{left:910px;background:var(--c4-body)}.c4 .col-head{background:var(--c4-head)}
.c2 .cons li:first-child{margin-bottom:8px}
</style>
</head>
<body>
<svg width="0" height="0" style="position:absolute">
  <defs>
    <symbol id="tick" viewBox="0 0 14 14"><circle cx="7" cy="7" r="6" fill="none" stroke="var(--tick)" stroke-width="1.4"/><path d="M4.2 7.2l2 2 3.6-4" fill="none" stroke="var(--tick)" stroke-width="1.4" stroke-linecap="round" stroke-linejoin="round"/></symbol>
    <symbol id="cross" viewBox="0 0 14 14"><circle cx="7" cy="7" r="6" fill="none" stroke="var(--cross)" stroke-width="1.4"/><path d="M4.8 4.8l4.4 4.4M9.2 4.8l-4.4 4.4" stroke="var(--cross)" stroke-width="1.4" stroke-linecap="round"/></symbol>
  </defs>
</svg>

<h1 class="headline">There are <b>3 major monetization models</b><br>that have begun to gain traction with AI,<br>and one we expect to see more of</h1>
<div class="brand"><span class="brand-mark"></span>Strelquin</div>

<div class="panel"></div>
<div class="row-band" style="top:398px;height:36px"></div>
<div class="row-band" style="top:437px;height:46px"></div>
<div class="row-band" style="top:486px;height:34px"></div>
<div class="row-band" style="top:524px;height:46px"></div>
<div class="row-band" style="top:574px;height:34px"></div>
<div class="row-band" style="top:610px;height:80px"></div>
<div class="row-band" style="top:694px;height:34px"></div>
<div class="row-band" style="top:730px;height:120px"></div>

<div class="tag-shadow"></div>
<div class="tag">Challenges of GenAI Monetization</div>
<div class="group-label now">Frequently seen today</div>
<div class="group-label future">Future option?</div>

<div class="row-label" style="top:403px">Description</div>
<div class="row-label" style="top:487px">Examples</div>
<div class="row-label" style="top:575px">Pros</div>
<div class="row-label" style="top:696px">Cons</div>

<section class="col c1">
  <div class="col-head">USER<br>LICENSES</div>
  <p class="cell desc">Charge a flat price for a user to have access to the functionality</p>
  <div class="cell ex"><span class="ex-name"><i></i>Vexachat</span><span class="ex-name"><i></i>Quillorb</span></div>
  <ul class="cell pros"><li><svg><use href="#tick"/></svg>Simple and easily understood</li></ul>
  <ul class="cell cons" style="padding-right:40px">
    <li><svg><use href="#cross"/></svg>High price limits adoption</li>
    <li style="margin-bottom:11px;white-space:nowrap"><svg><use href="#cross"/></svg>Not tightly value aligned</li>
    <li style="padding-right:0;margin-right:-40px"><svg><use href="#cross"/></svg>Risky if fair usage restriction is not placed on</li>
    <li><svg><use href="#cross"/></svg>Upsell dependent on wider adoption</li>
  </ul>
</section>

<section class="col c2">
  <div class="col-head">USAGE-BASED<br>TOKENS</div>
  <p class="cell desc">Purchase blocks of tokens that can be spend on usage/work of the AI functionality</p>
  <div class="cell ex"><span class="ex-name"><i></i>Torvanix</span><span class="ex-name"><i></i>Glenvarro Vision API</span></div>
  <ul class="cell pros" style="padding-right:44px">
    <li><svg><use href="#tick"/></svg>Covers costs at all scales of usage</li>
    <li><svg><use href="#tick"/></svg>Tokens help with predictability issues</li>
  </ul>
  <ul class="cell cons" style="padding-left:12px;padding-right:36px">
    <li><svg><use href="#cross"/></svg>Not tightly value aligned (value may not increase linearly with usage)</li>
    <li><svg><use href="#cross"/></svg>Not ARR</li>
  </ul>
</section>

<section class="col c3">
  <div class="col-head">OUTCOME<br>BASED</div>
  <p class="cell desc">Pay for the outcomes of the GenAI functionality</p>
  <div class="cell ex"><span class="ex-name lg"><i></i>claimvesta</span><span class="ex-name"><i></i>helpquarry</span></div>
  <ul class="cell pros" style="padding-left:12px;padding-right:60px"><li><svg><use href="#tick"/></svg>Potentially highly value-aligned</li></ul>
  <ul class="cell cons" style="padding-left:12px;padding-right:70px">
    <li><svg><use href="#cross"/></svg>Delayed revenue realization</li>
    <li><svg><use href="#cross"/></svg>Tough to find the right metric</li>
    <li><svg><use href="#cross"/></svg>Not ARR</li>
  </ul>
</section>

<section class="col c4">
  <div class="col-head">USAGE-TIERED<br>LICENSES</div>
  <p class="cell desc" style="padding-left:16px;padding-right:36px">Offer different user licenses with different usage capacities</p>
  <div class="cell ex"><span class="ex-name"><i></i>Vexachat</span></div>
  <ul class="cell pros" style="padding-left:10px">
    <li><svg><use href="#tick"/></svg>Value aligned</li>
    <li><svg><use href="#tick"/></svg>Simple &amp; predictable</li>
    <li><svg><use href="#tick"/></svg>Natural upsell path</li>
    <li><svg><use href="#tick"/></svg>Low barrier to adoption</li>
  </ul>
  <ul class="cell cons" style="padding-left:10px;padding-right:80px"><li><svg><use href="#cross"/></svg>Limit on the number of tiers</li></ul>
</section>
</body>
</html>
```